TQ27 Computer Produced for Poultry Houses needs a Corporate Touch

We need a unique screen design with unique graphics for our new product called "TQ27". TQ27 product is a computer produced for poultry houses. It has a LED screen on which user can change settings for heating, air quaility, inside temprateure, cooling, pressure etc as defined in the attached pictures.

We need 6 designs for the following :

1- TQ27 BOX Front Cover Design
2- LED Screen Main Menu
3- LED Screen Inner Menu
4- LED Screen Main Page Menu
5- Vector Logo (JPEG is included, will be prepared in vectorel format)
6- Stationery Design

Explanations are defined below:

1- TQ27 BOX Front Cover Design: This box is 37cm width and 47 cm height. It has a LED screen (19 cm x 14cm) in the middle and 3 circular buttons under the LED screen as seenin the attachment. We need a simple but good quality design including corporate colors (dark blue and red) for this box only for the front face of the box.

Attached pictures : 1-a.jpg 1-b.jpg 1-c.jpg (example)

2- LED Screen Main Menu : LED screen (8.7 cm x 15.5 cm) and a border. This menu includes 12 main menu buttons. You will design 12 menu buttons. This menu should look like panelix start menu or orbifon menu with icons.
a- Values
b- Air Conditioning
c- Heating
d- Alarm
e- Fans
f- Cooling
g-Pressure
h-Timing
i- Reports
j- Close Lights
k- Weights
l- Management (Admin)

Attached pictures : 2-a.jpg 2-b.jpg LEDDimensions.jpg

3- LED Screen Inner Menu : This screen is one example inner menu when clicked on one of icons defined in (2). You will design up and down arrows, textbox and "Go to back" button and "Go to Home" button and final screen design (placement)

Attached pictures : 3-a.jpg

4- LED Screen Main Page Menu : This menu has a poultry house drawing with summary information boxes above.

You will submit the main page design.

Additionally, We need 3 GIF pictures with animation (defined in 4-a.jpg)
a- Moving fans (turning)
b- Fire (burning)
c- Pets (dropping wet drops down on the pad - brown rectangular area)
Attached pictures : 4-a.jpg

Poultry house has 10 fans all in one row. and 6 fans on the long side.

5- Vector logo : In this part, you will submit 2 vectorel logos. First, you will design Vectorel format of velmora_logo.png (attached) and PNG format. And will design TQ27 logo with same structure, fonts, puntos.

6- Stationery Design : Cardvisit + Letter design + Company headed paper

Computer

0456a4
ef363c
add136

• Flat design, best user experience

```html
<!DOCTYPE html>
<html lang="en">
<head>
<meta charset="utf-8">
<title>TQ27 Box Front Cover</title>
<link rel="stylesheet" href="https://fonts.googleapis.com/css2?family=Montserrat:wght@700&display=swap">
<style>
  :root {
    --brand-blue: #1897d2;
    --brand-slate: #4a5b6a;
    --band-white: #ffffff;
    --device-black: #040708;
  }
  html, body {
    margin: 0;
    padding: 0;
    width: 945px;
    height: 1200px;
    overflow: hidden;
  }
  .box-front {
    position: relative;
    width: 945px;
    height: 1200px;
    background: var(--band-white);
    overflow: hidden;
  }
  .box-front__bands {
    position: absolute;
    inset: 0;
    width: 945px;
    height: 1200px;
  }
  .band-blue { fill: var(--brand-blue); }
  .band-slate { fill: var(--brand-slate); }
  .led-screen {
    position: absolute;
    left: 228px;
    top: 281px;
    width: 489px;
    height: 280px;
    background: var(--device-black);
    border-radius: 12px;
  }
  .control-buttons {
    position: absolute;
    left: 281px;
    top: 832px;
    display: flex;
    gap: 74px;
  }
  .control-button {
    width: 78px;
    height: 78px;
    border-radius: 50%;
    background: var(--device-black);
  }
  .brand-mark {
    position: absolute;
    left: 98px;
    top: 1040px;
    display: flex;
    align-items: center;
    gap: 14px;
    color: var(--band-white);
  }
  .brand-mark__square {
    width: 56px;
    height: 56px;
    background: var(--band-white);
  }
  .brand-mark__name {
    font-family: "Montserrat", sans-serif;
    font-weight: 700;
    font-size: 50px;
    line-height: 1;
    letter-spacing: 1px;
  }
</style>
</head>
<body>
  <main class="box-front">
    <svg class="box-front__bands" viewBox="0 0 945 1200" aria-hidden="true">
      <polygon class="band-blue" points="0,0 330,0 420,1200 0,1200"/>
      <polygon class="band-slate" points="600,0 945,0 945,1200 720,1200"/>
    </svg>

    <div class="led-screen"></div>

    <div class="control-buttons">
      <div class="control-button"></div>
      <div class="control-button"></div>
      <div class="control-button"></div>
    </div>

    <div class="brand-mark">
      <div class="brand-mark__square"></div>
      <span class="brand-mark__name">TQ27</span>
    </div>
  </main>
</body>
</html>
```